Business Card Design

Im electrician in melbourne after a business cards. I have no logos done. I have attached a card that i like but needs to be altered to my business name, so in the picture shows a lead plug into a socket spelling plug, i want the spelling replaced with my company name. I was thinking some thing with a charcoal back ground with yellow or green font.
I have wrote what I'd like above but feel free to try your own ideas and designs.
Industry/Entity Type
Electrician
Contact Information for Business Card
Zul Electrical Services PTY LTD (Display on the front of card, the PTY LTD can be in small font)
REC:58142 (also on the front in small font)
Call Dario (back i dont want my last name on the card)
Phone: 0488157093 (back
Email: zulelectricalservices@kestrelmail.net (back)
Domestic, Commercial, Industrial, (on the back in dot points.)
Look and feel
Each slider illustrates characteristics of the customer's brand and the style your logo design should communicate.

```html
<!DOCTYPE html>
<html lang="en">
<head>
<meta charset="utf-8">
<title>Zul Electrical Services – Business Card</title>
<link rel="stylesheet" href="https://fonts.googleapis.com/css2?family=Titillium+Web:wght@300;400&display=swap">
<style>
  :root {
    --charcoal: #454142;
    --lime: #9dcc4e;
    --paper: #ffffff;
    --text-font: "Titillium Web", sans-serif;
  }
  * { margin: 0; padding: 0; box-sizing: border-box; }
  html, body {
    width: 952px;
    height: 1200px;
    overflow: hidden;
    background: var(--paper);
    font-family: var(--text-font);
  }
  .sheet { position: relative; width: 952px; height: 1200px; }

  .card { position: absolute; left: 0; width: 952px; height: 573px; }
  .card--front { top: 0; background: var(--charcoal); }
  .card--back { top: 627px; background: var(--lime); }

  .brand {
    position: absolute;
    left: 69px;
    top: 176px;
    display: flex;
    align-items: center;
    gap: 22px;
  }
  .brand__mark {
    width: 48px;
    height: 44px;
    background: var(--lime);
    border-radius: 6px;
  }
  .brand__name {
    color: var(--lime);
    font-weight: 300;
    font-size: 60px;
    line-height: 1;
    letter-spacing: 1px;
  }
  .registration {
    position: absolute;
    left: 578px;
    top: 274px;
    color: var(--lime);
    font-weight: 400;
    font-size: 20px;
    word-spacing: 6px;
  }
  .services-band {
    position: absolute;
    left: 0;
    top: 426px;
    width: 952px;
    height: 48px;
    background: var(--lime);
    color: var(--charcoal);
    font-size: 31px;
    font-weight: 400;
    letter-spacing: 6px;
    line-height: 48px;
    padding-left: 100px;
    white-space: nowrap;
  }

  .call {
    position: absolute;
    left: 282px;
    top: 118px;
    color: var(--charcoal);
    font-size: 46px;
    font-weight: 400;
  }
  .contact-name {
    position: absolute;
    left: 282px;
    top: 179px;
    display: flex;
    align-items: center;
    gap: 28px;
  }
  .contact-name__mark {
    width: 66px;
    height: 66px;
    background: var(--charcoal);
    border-radius: 8px;
  }
  .contact-name__text {
    color: var(--charcoal);
    font-weight: 300;
    font-size: 104px;
    line-height: 1;
  }
  .phone-band {
    position: absolute;
    left: 0;
    top: 422px;
    width: 952px;
    height: 53px;
    background: var(--charcoal);
    color: var(--lime);
    font-size: 33px;
    line-height: 53px;
    text-align: center;
  }
  .email {
    position: absolute;
    left: 0;
    top: 482px;
    width: 952px;
    color: var(--charcoal);
    font-size: 33px;
    text-align: center;
  }
</style>
</head>
<body>
<main class="sheet">
  <section class="card card--front">
    <div class="brand">
      <span class="brand__mark"></span>
      <span class="brand__name">Zul Electrical Services</span>
    </div>
    <p class="registration">PTY LTD&nbsp; REC:58142</p>
    <p class="services-band">Domestic&nbsp; |&nbsp; Commercial&nbsp; |&nbsp; Industrial</p>
  </section>

  <section class="card card--back">
    <p class="call">Call</p>
    <div class="contact-name">
      <span class="contact-name__mark"></span>
      <span class="contact-name__text">Dario</span>
    </div>
    <p class="phone-band">Phone: 0488157093</p>
    <p class="email">Email: zulelectricalservices@kestrelmail.net</p>
  </section>
</main>
</body>
</html>
```